Sale of South Sea and Tahitian Pearl Jewellery, online business

I need a business card designed for my website business. We sell South Sea and Tahitian Pearl Jewellery. The colour theme for the website is black and white and would like to carry this through to business cards. Our brand is very elegant and stylish, would like sketch picture of women or fashion involving pearls if not the sketched picture then have the card very plan. below are pictures of the ideas I like and also the logo and writing that is used on my jewellery boxes.
Font is English Hand DB

Target Market(s)

30 and over women in the high end of the market

Industry/Entity Type

Business

Contact Information for Business Card

Business name - Varno Gems( front of card)
Back of card -Details
Rosalind Thackery
Gemmologist MDRS
email: rosalind@varnogems.com.au
website: varnogems.com.au
mob: +61 427 508 193
Perth Australia

Varno Stelle PTY T/AS Varno Gems
ABN 47 283 915 604

Colors
1b1b1b
ffffff
85cae6

Requirements
Must have
• Black and white colour preferably black card with white writing and picture.
• The Same writing as logo and writing on box packaging, attached a file with writing.
• Business name on one side of the card and all other details on the other side.
• Can have tiny hints of the harbour blue colour.
• Font: English Hand DB
Nice to have
• I really like the idea of having a sketch of a stylish or elegent lady wearing pearls or a sketch of a pearl, if not the sketch a really plain and simple card.
Should not have
• busy patterns.

```html
<!DOCTYPE html>
<html lang="en">
<head>
<meta charset="utf-8">
<title>Varno Gems – Business Card</title>
<link rel="stylesheet" href="https://fonts.googleapis.com/css2?family=Source+Sans+3:wght@300;400;600&display=swap">
<style>
  :root {
    --page: #e9e7e3;
    --silver-light: #bdbdbd;
    --silver-dark: #9c9c9c;
    --ink: #1b1b1b;
    --black: #0c0c0c;
    --black-soft: #262626;
    --white: #ffffff;
    --grey-text: #b8b8b8;
    --accent: #85cae6;
  }
  * { box-sizing: border-box; margin: 0; padding: 0; }
  html, body { width: 1200px; height: 950px; overflow: hidden; }
  body {
    background: var(--page);
    font-family: "Source Sans 3", sans-serif;
    position: relative;
  }
  .card {
    position: absolute;
    left: 250px;
    width: 700px;
    height: 400px;
    border-radius: 22px;
    overflow: hidden;
    box-shadow: 0 10px 30px rgba(0,0,0,0.18);
  }
  /* Front */
  .card-front {
    top: 45px;
    background: linear-gradient(160deg, var(--silver-light), var(--silver-dark));
    color: var(--ink);
  }
  .front-ring {
    position: absolute;
    left: 330px; top: 40px;
    width: 250px; height: 250px;
    border: 4px solid var(--ink);
    border-radius: 50%;
  }
  .front-name {
    position: absolute;
    left: 60px; top: 280px;
    font-size: 54px;
    font-weight: 400;
    letter-spacing: 3px;
  }
  .front-url {
    position: absolute;
    left: 64px; top: 350px;
    font-size: 17px;
    letter-spacing: 4px;
  }
  /* Back */
  .card-back {
    top: 505px;
    background: linear-gradient(150deg, var(--black-soft) 0%, var(--black) 55%, #161616 100%);
    color: var(--white);
  }
  .brand-lockup {
    position: absolute;
    right: 50px; top: 50px;
    display: flex;
    align-items: center;
    gap: 18px;
  }
  .brand-ring {
    width: 62px; height: 62px;
    border: 2px solid var(--white);
    border-radius: 50%;
  }
  .brand-divider { width: 2px; height: 62px; background: var(--white); }
  .brand-name { font-size: 40px; font-weight: 400; letter-spacing: 2px; }
  .rule {
    position: absolute;
    right: 50px; top: 140px;
    width: 330px; height: 1px;
    background: var(--grey-text);
  }
  .company {
    position: absolute;
    right: 50px; top: 158px;
    text-align: right;
    font-size: 17px;
    line-height: 1.45;
    color: var(--white);
    font-weight: 300;
  }
  .person { position: absolute; left: 60px; top: 218px; }
  .person-name { font-size: 26px; font-weight: 600; }
  .person-title { font-size: 17px; font-weight: 300; color: var(--grey-text); margin-top: 2px; }
  .contact-list {
    position: absolute;
    left: 60px; top: 285px;
    list-style: none;
    font-size: 17px;
    font-weight: 300;
    line-height: 1.6;
  }
  .contact-list li { display: flex; align-items: center; gap: 10px; }
  .contact-list svg { width: 16px; height: 16px; flex: none; }
  .bottom-band {
    position: absolute;
    left: 0; right: 0; bottom: 0;
    height: 12px;
    background: var(--white);
  }
  .bottom-band::after {
    content: "";
    position: absolute;
    right: 0; top: 0; bottom: 0;
    width: 28%;
    background: var(--grey-text);
  }
</style>
</head>
<body>
  <section class="card card-front" aria-label="Card front">
    <div class="front-ring"></div>
    <div class="front-name">Varno Gems</div>
    <div class="front-url">www.varnogems.com.au</div>
  </section>

  <section class="card card-back" aria-label="Card back">
    <div class="brand-lockup">
      <div class="brand-ring"></div>
      <div class="brand-divider"></div>
      <div class="brand-name">Varno Gems</div>
    </div>
    <div class="rule"></div>
    <div class="company">
      Perth Australia<br>
      ABN 47 283 915 604<br>
      Varno Stelle PTY T/AS Varno Gems
    </div>

    <div class="person">
      <div class="person-name">Rosalind Thackery</div>
      <div class="person-title">Gemmologist MDRS</div>
    </div>

    <ul class="contact-list">
      <li>
        <svg viewBox="0 0 16 16" aria-hidden="true"><rect x="4" y="1" width="8" height="14" rx="1.5" fill="none" stroke="#fff" stroke-width="1.4"/><line x1="7" y1="12.5" x2="9" y2="12.5" stroke="#fff" stroke-width="1.2"/></svg>
        +61 427 508 193
      </li>
      <li>
        <svg viewBox="0 0 16 16" aria-hidden="true"><rect x="1" y="3" width="14" height="10" fill="#fff"/><polyline points="1,3 8,9 15,3" fill="none" stroke="#0c0c0c" stroke-width="1.4"/></svg>
        rosalind@varnogems.com.au
      </li>
      <li>
        <svg viewBox="0 0 16 16" aria-hidden="true"><circle cx="8" cy="8" r="7" fill="none" stroke="#fff" stroke-width="1.4"/><ellipse cx="8" cy="8" rx="3" ry="7" fill="none" stroke="#fff" stroke-width="1"/><line x1="1" y1="8" x2="15" y2="8" stroke="#fff" stroke-width="1"/></svg>
        www.varnogems.com.au
      </li>
    </ul>
    <div class="bottom-band"></div>
  </section>
</body>
</html>
```